Financial Sevices firm looking for Brochure design

Our company Veltmoor Capital and Holdings Limited (VeltHoldings)
i
Is an investment/advisory firm - www.veltholdings-grp.net
We invest in the energy sector in Africa and offer advisory services to Energy companies looking to invest in Africa. From oil and gas, to renewables (wind/solar). We are more focused on the "West African" Sub region
We need corporate brochure (Booklet style) to circulate to our corporate clients
We would like to see a design that considers the colours in our Logo (see website)
HI Guys, sorry been travelling. Seen some very good submissions and will be sending updates shortly
Reason: Dear Designers,
Thank you for participating in this project and for some of the great designs i've received so far. Unfortunately, due to the holidays, it has been difficult to consult with other members of my team. As a result, the project deadline is extended by about 12 days
I appreciate your understanding in the situation and looking forward to continuing the excellent collaboration in the coming days
Reason: Hi All,
Apologies for the multiple deadline extensions and thanks so much for all the designs which my team and I will be reviewing today and tomorrow.
We will be closing this project tomorrow by 6pm GMT (17th Jan 2014)
Thanks to all those that submitted such wonderful designs and goodluck!!
Project to be closed finally on 17th Jan 2014 at 6pm GMT
Banks, Investment Firms, Energy companies, Private Equity Funds
I have attached a Brochure that I created myself as an example of the type of information required but please also feel free to visit our website www.veltholdings-grp.net
Looking for any creative ideas you have to suplement the information provided.
Financial

```html
<!DOCTYPE html>
<html lang="en">
<head>
<meta charset="utf-8">
<title>VeltHoldings – Brochure Spread</title>
<link href="https://fonts.googleapis.com/css2?family=Exo+2:wght@400;600;700&display=swap" rel="stylesheet">
<style>
  :root {
    --backdrop: #1d1d1f;
    --red-deep: #8e141b;
    --red-mid: #b21d26;
    --red-bright: #d6252e;
    --orange: #f6a21e;
    --orange-light: #fbb43a;
    --paper-white: #f3f3f3;
    --text-white: #ffffff;
    --text-orange: #f7a823;
  }
  * { margin: 0; padding: 0; box-sizing: border-box; }
  html, body {
    width: 1200px;
    height: 750px;
    overflow: hidden;
    background: var(--backdrop);
    font-family: "Exo 2", "Segoe UI", sans-serif;
  }
  .spread {
    position: absolute;
    left: 120px;
    top: 36px;
    width: 858px;
    height: 606px;
    transform: scale(1.119);
    transform-origin: top left;
    overflow: hidden;
  }
  .spread__pattern,
  .spread__shapes {
    position: absolute;
    inset: 0;
    width: 858px;
    height: 606px;
  }
  .page-intro {
    position: absolute;
    left: 61px;
    top: 298px;
    width: 296px;
    text-align: center;
    font-size: 8.4px;
    line-height: 11px;
    color: var(--text-orange);
  }
  .page-intro strong,
  .competency strong,
  .competencies-lead {
    color: var(--text-white);
    font-weight: 700;
  }
  .competencies-lead {
    position: absolute;
    left: 433px;
    top: 292px;
    width: 200px;
    text-align: center;
    font-size: 8.6px;
    line-height: 11px;
    font-weight: 400;
  }
  .competencies-title {
    display: block;
    margin-top: 3px;
    font-size: 17px;
    line-height: 18px;
    font-weight: 600;
    letter-spacing: 0.6px;
  }
  .competency-list {
    position: absolute;
    left: 643px;
    top: 249px;
    width: 180px;
    list-style: none;
  }
  .competency {
    font-size: 8.2px;
    line-height: 10.8px;
    color: var(--text-orange);
    margin-bottom: 12px;
  }
</style>
</head>
<body>
  <main class="spread">
    <svg class="spread__pattern" viewBox="0 0 858 606" role="img" aria-label="Low-poly pattern of faceted red triangles across both pages">
      <defs>
        <linearGradient id="redField" x1="0" y1="0" x2="1" y2="1">
          <stop offset="0" stop-color="#a8161f"/>
          <stop offset="0.35" stop-color="#b91e27"/>
          <stop offset="0.6" stop-color="#9b1820"/>
          <stop offset="1" stop-color="#c8212b"/>
        </linearGradient>
      </defs>
      <rect width="858" height="606" fill="url(#redField)"/>
    </svg>
    <svg class="spread__shapes" viewBox="0 0 858 606" aria-hidden="true">
      <defs>
        <linearGradient id="fold" x1="0" y1="0" x2="1" y2="0">
          <stop offset="0" stop-color="#000" stop-opacity="0"/>
          <stop offset="0.45" stop-color="#000" stop-opacity="0.28"/>
          <stop offset="0.5" stop-color="#000" stop-opacity="0.4"/>
          <stop offset="0.55" stop-color="#fff" stop-opacity="0.06"/>
          <stop offset="1" stop-color="#000" stop-opacity="0"/>
        </linearGradient>
        <linearGradient id="orangeBand" x1="0" y1="0" x2="1" y2="1">
          <stop offset="0" stop-color="var(--orange-light)"/>
          <stop offset="1" stop-color="var(--orange)"/>
        </linearGradient>
      </defs>
      <polygon class="corner corner--white" points="0,0 113,0 0,40" fill="var(--paper-white)"/>
      <polygon class="corner corner--orange" points="430,0 858,0 858,55 759,116 612,70" fill="url(#orangeBand)"/>
      <polygon class="corner corner--orange" points="0,550 225,606 0,606" fill="url(#orangeBand)"/>
      <polygon class="corner corner--white" points="396,606 504,540 650,606" fill="var(--paper-white)"/>
      <rect class="fold-shade" x="380" y="0" width="90" height="606" fill="url(#fold)"/>
      <path class="bracket" d="M656 220 H634 Q628 220 628 226 V392 Q628 398 634 398 H656" fill="none" stroke="var(--orange)" stroke-width="1"/>
      <circle cx="656" cy="220" r="2" fill="var(--orange)"/>
      <circle cx="656" cy="398" r="2" fill="var(--orange)"/>
    </svg>

    <p class="page-intro"><strong>VeltHoldings</strong> is an indigenous investment and advisory firm with global networks and international expertise in infrastructure project finance.</p>

    <p class="competencies-lead">VeltHoldings seeks to add<br>value to its clients through its core
      <span class="competencies-title">COMPETENCIES</span></p>

    <ul class="competency-list">
      <li class="competency"><strong>Unique ability to deliver tailor-made solutions</strong> including structuring project and operating capital, project budget analysis, modeling, securing attractively-priced capital.</li>
      <li class="competency"><strong>Collective experience in originating, appraising, structuring, and financing investments</strong> in infrastructure assets worth over US$ 10 billion across Africa.</li>
    </ul>
  </main>
</body>
</html>
```